Business Card Design for Quillmoreton Carpentry

I need a business card design for my carpentry company Quillmoreton Carpentry. Ive attached files with all information I require on both sides. Look forward to seeing your design.

```html
<!DOCTYPE html>
<html lang="en">
<head>
<meta charset="utf-8">
<title>Quillmoreton Carpentry – Business Card</title>
<link rel="stylesheet" href="https://fonts.googleapis.com/css2?family=Arimo:wght@400;700&display=swap">
<style>
  :root {
    --stage: #2b2b2b;
    --paper: #ffffff;
    --orange: #e2531f;
    --orange-deep: #cf4718;
    --ink: #262626;
    --ink-soft: #3a3a3a;
  }
  * { box-sizing: border-box; margin: 0; padding: 0; }
  html, body {
    width: 1200px; height: 997px; overflow: hidden;
    background: var(--stage);
    font-family: "Arimo", Arial, sans-serif;
  }
  .stage { position: relative; width: 1200px; height: 997px; }

  .card {
    position: absolute;
    width: 560px; height: 320px;
    background: var(--paper);
    overflow: hidden;
    box-shadow: 0 10px 30px rgba(0,0,0,.45);
  }
  .card--services { left: 50px; top: 110px; }
  .card--contact { left: 590px; top: 520px; }

  /* brand lockup */
  .rule { position: absolute; height: 4px; background: var(--orange); }
  .rule--thin { height: 2px; }
  .dot {
    position: absolute; width: 14px; height: 14px; border-radius: 50%;
    background: var(--orange);
  }
  .brand-name {
    position: absolute; left: 0; right: 0; top: 86px;
    text-align: center;
    font-weight: 700; font-size: 31px; letter-spacing: 2px;
    text-transform: uppercase; color: var(--ink);
  }

  /* bottom band */
  .band {
    position: absolute; left: 0; right: 0; bottom: 0;
    background: var(--orange);
  }
  .band::before {
    content: ""; position: absolute; left: 0; right: 0; top: 6px;
    height: 2px; background: var(--paper);
  }
  .band-line { position: absolute; left: 0; right: 0; height: 3px; background: var(--orange); }

  .tagline {
    position: absolute; left: 0; right: 0; bottom: 18px;
    text-align: center; color: var(--paper);
    font-weight: 700; font-size: 16px; letter-spacing: 1px;
    text-transform: uppercase;
  }

  .services {
    position: absolute; left: 0; right: 0; bottom: 20px;
    text-align: center; color: var(--paper);
    font-size: 13px; line-height: 19px; letter-spacing: .3px;
  }

  /* contact details */
  .contact-icons {
    position: absolute; left: 0; right: 0; top: 172px;
    display: flex; justify-content: center; gap: 14px;
  }
  .contact-icons svg { width: 18px; height: 18px; }
  .contact-lines {
    position: absolute; left: 0; right: 0; top: 200px;
    text-align: center; color: var(--ink-soft);
    font-size: 15px; line-height: 24px;
  }
</style>
</head>
<body>
<main class="stage">

  <section class="card card--services" aria-label="Business card, services side">
    <div class="rule" style="left:150px; right:60px; top:66px;"></div>
    <div class="dot" style="right:30px; top:61px;"></div>
    <p class="brand-name">Quillmoreton Carpentry</p>
    <div class="rule" style="left:60px; right:150px; top:136px;"></div>
    <div class="rule rule--thin" style="left:60px; right:150px; top:146px;"></div>
    <div class="dot" style="left:30px; top:136px;"></div>

    <div class="band-line" style="top:196px;"></div>
    <div class="band" style="height:110px;">
      <p class="services">
        Decks &amp; Pergolas &bull; Shop Fitout &bull; Wall &amp; Roof Framing &bull; Refurbishment<br>
        Doors &amp; Windows &bull; Fences/Gates &bull; Attic Conversions &bull; Privacy Screens<br>
        Timber Flooring &bull; Wall Cladding &bull; Extensions &amp; More...
      </p>
    </div>
  </section>

  <section class="card card--contact" aria-label="Business card, contact side">
    <div class="rule" style="left:150px; right:60px; top:66px;"></div>
    <div class="dot" style="right:30px; top:61px;"></div>
    <p class="brand-name">Quillmoreton Carpentry</p>
    <div class="rule" style="left:60px; right:150px; top:136px;"></div>
    <div class="rule rule--thin" style="left:60px; right:150px; top:146px;"></div>
    <div class="dot" style="left:30px; top:136px;"></div>

    <div class="contact-icons">
      <svg viewBox="0 0 20 20" aria-label="Phone" role="img">
        <circle cx="10" cy="10" r="10" fill="var(--orange)"/>
        <path d="M6 5.5c.6-.6 1.3-.5 1.7.1l.9 1.5c.3.5.2 1-.2 1.3l-.6.5c.6 1.3 1.5 2.2 2.8 2.8l.5-.6c.3-.4.8-.5 1.3-.2l1.5.9c.6.4.7 1.1.1 1.7l-.7.7C11.7 15.3 4.7 8.3 5.3 6.2z" fill="#fff"/>
      </svg>
      <svg viewBox="0 0 20 20" aria-label="Email" role="img">
        <circle cx="10" cy="10" r="10" fill="var(--orange)"/>
        <rect x="5" y="6.5" width="10" height="7" fill="#fff"/>
        <path d="M5 6.5l5 4 5-4" fill="none" stroke="var(--orange)" stroke-width="1.2"/>
      </svg>
    </div>
    <p class="contact-lines">
      0400 555 019<br>
      hello@quillmoretoncarpentry.com
    </p>

    <div class="band-line" style="top:246px;"></div>
    <div class="band" style="height:62px;">
      <p class="tagline">Anything carpentry. Anywhere in Sydney</p>
    </div>
  </section>

</main>
</body>
</html>
```